Zielgruppe
Ich bin eine junge Fotografin und tätig in folgenden Bereichen:
- Hochzeits-Fotografie
- Outdoor-Fotografie
- Studio-Fotografie
Aufgabenstellung
Die Seite soll freundlich, professionell und übersichtlich sein.
Die Seite soll von den Bildern leben. Emotionen vermitteln.
Responsive Design ist mir wichtig, im nachhinein möchte ich die Seite Programmieren lassen damit ich mit Wordpress arbeiten kann und die Seite soll gut Suchmaschinenoptimiert werden.

```html
<!DOCTYPE html>
<html lang="de">
<head>
<meta charset="utf-8">
<title>Velvet Lantern – Willkommen</title>
<link href="https://fonts.googleapis.com/css2?family=Titillium+Web:wght@300;400;600;700&display=swap" rel="stylesheet">
<style>
  :root {
    --crimson: #c8274a;
    --crimson-deep: #8e1a36;
    --crimson-dark: #5e1026;
    --white: #ffffff;
    --nav-text: #4a4a4a;
  }
  * { margin: 0; padding: 0; box-sizing: border-box; }
  html, body {
    width: 1200px;
    height: 799px;
    overflow: hidden;
    background: var(--white);
    font-family: "Titillium Web", Arial, sans-serif;
  }
  .page {
    position: relative;
    width: 1200px;
    height: 799px;
    background: var(--white);
  }
  .site-header {
    position: relative;
    height: 76px;
    z-index: 2;
  }
  .brand {
    position: absolute;
    left: 56px;
    top: 0;
    width: 112px;
    height: 102px;
    display: flex;
    align-items: center;
    justify-content: center;
  }
  .brand::before {
    content: "";
    position: absolute;
    left: 0;
    bottom: 0;
    width: 112px;
    height: 112px;
    border-radius: 50%;
    background: var(--white);
  }
  .brand-name {
    position: relative;
    margin-top: -22px;
    color: var(--crimson);
    font-weight: 700;
    font-size: 19px;
    line-height: 1;
    text-align: center;
  }
  .main-nav {
    position: absolute;
    right: 66px;
    top: 30px;
    display: flex;
    gap: 26px;
  }
  .main-nav a {
    font-size: 9px;
    font-weight: 600;
    color: var(--nav-text);
    text-decoration: none;
    padding-bottom: 3px;
  }
  .main-nav a.is-active {
    color: var(--crimson);
    border-bottom: 1px solid var(--crimson);
  }
  .hero {
    position: absolute;
    left: 49px;
    top: 76px;
    width: 1110px;
    height: 630px;
    overflow: hidden;
  }
  .hero-photo {
    position: absolute;
    inset: 0;
    background:
      radial-gradient(ellipse 40% 60% at 52% 45%, var(--crimson) 0%, rgba(200,39,74,0) 70%),
      linear-gradient(100deg, var(--crimson-dark) 0%, var(--crimson-deep) 22%, var(--crimson) 50%, var(--crimson-deep) 78%, var(--crimson-dark) 100%);
  }
  .hero-content {
    position: absolute;
    left: 0;
    right: 0;
    top: 232px;
    text-align: center;
    color: var(--white);
  }
  .hero-title {
    font-weight: 300;
    font-size: 40px;
    line-height: 42px;
    letter-spacing: 0.5px;
  }
  .hero-byline {
    margin-top: 16px;
    font-weight: 600;
    font-size: 11px;
  }
  .hero-button {
    display: inline-block;
    margin-top: 28px;
    width: 100px;
    height: 25px;
    line-height: 25px;
    background: var(--white);
    color: var(--crimson);
    font-size: 9px;
    font-weight: 700;
    letter-spacing: 1px;
    text-decoration: none;
  }
  .slider-dots {
    position: absolute;
    left: 0;
    right: 0;
    bottom: 14px;
    display: flex;
    justify-content: center;
    gap: 5px;
  }
  .slider-dots span {
    width: 7px;
    height: 7px;
    border-radius: 50%;
    border: 1px solid var(--white);
  }
  .slider-dots span.is-current { background: var(--white); }
</style>
</head>
<body>
<div class="page">
  <header class="site-header">
    <div class="brand"><span class="brand-name">Velvet<br>Lantern</span></div>
    <nav class="main-nav">
      <a href="#" class="is-active">Willkommen</a>
      <a href="#">Hinter Der Linse</a>
      <a href="#">Portfolio</a>
      <a href="#">Angebote</a>
      <a href="#">Kontakt</a>
    </nav>
  </header>

  <section class="hero">
    <div class="hero-photo" role="img" aria-label="Porträtfoto der Fotografin mit Kamera vor einer Holzwand, rot eingefärbt"></div>
    <div class="hero-content">
      <h1 class="hero-title">Herzlich Willkommen<br>in der Welt der Fotografie</h1>
      <p class="hero-byline">Lena Brunner, Fotografin, 35 Jahre alt</p>
      <a href="#" class="hero-button">Mehr Erfahren</a>
    </div>
    <div class="slider-dots">
      <span class="is-current"></span><span></span><span></span><span></span>
    </div>
  </section>
</div>
</body>
</html>
```